Web Design for Independent Pet Supply shop.

Larkfield Critter Depot is a locally owned and operated premium natural pet food store and supply company with 2 thriving retail stores in Bend, Oregon, and a home delivery service. The pet food offered is the best on the market and may be described as “holistic”. Also on offer is a vast selection of toys, training tools, treats, and other supplies, as well as dog washing services that range from "do-it yourself" to "spa." Current site: LarkfieldCritterDepot.com. They need a new, updated and responsive site.
Likes:
Tovmira.com: Natural colors, not loud, pages in motion, simple & clean but very informative.
Dunmoregale.com: Everything in simple big colorful blocks. The specials run across the top and in motion. This site looks very professional but simple. The information is available several different places.
Quillbarrow.com: Again big blocks through out. Very Fun and inviting. Tons of information with videos and recipes and testimonials. Pleasant feel and colors as well.
Dislikes:
Zinvor.com: Looks cheap, hate the colors, very busy and over whelming. Hate the old style header bar going across with options. Too many printed words instead of fun images.
Colors should be "natural" tones, warm and soothing. Deep dark blue and greys with earthy wood color.
Do Not Use: Blue violet, violet, red violet

```html
<!DOCTYPE html>
<html lang="en">
<head>
<meta charset="utf-8">
<title>Larkfield Critter Depot</title>
<link rel="stylesheet" href="https://fonts.googleapis.com/css2?family=Lato:ital,wght@0,400;0,700;0,900;1,400&family=Questrial&display=swap">
<style>
:root{
  --wood:#b8873f;
  --wood-dark:#9c6f2e;
  --navy:#1f2d6e;
  --ink:#2b2b2b;
  --grey-text:#5a5a5a;
  --grey-band:#f2f2f2;
  --line:#d9d9d9;
  --footer:#121212;
  --footer-bottom:#0a0a0a;
  --white:#ffffff;
}
*{box-sizing:border-box;margin:0;padding:0}
html,body{width:1200px;height:2317px;overflow:hidden;background:var(--white)}
body{font-family:"Lato",Arial,sans-serif;color:var(--ink)}
.page{position:relative;width:1200px;height:2317px;overflow:hidden}
.abs{position:absolute}

/* header */
.site-header{left:0;top:0;width:1200px;height:102px;background:var(--white)}
.brand{left:94px;top:36px;display:flex;align-items:center;gap:8px;width:320px}
.brand-dot{width:26px;height:26px;border-radius:50%;background:var(--wood);flex:0 0 26px}
.brand-name{font-family:"Lato",sans-serif;font-weight:900;font-size:18px;line-height:26px;color:var(--wood);text-transform:uppercase;white-space:nowrap}
.main-nav{left:0;top:0;width:1200px;height:102px}
.main-nav a{position:absolute;top:52px;font-family:"Questrial",sans-serif;font-size:13px;line-height:16px;color:#777;text-decoration:none;text-transform:uppercase;white-space:nowrap}
.main-nav a.active{color:var(--wood)}
.main-nav a.active::after{content:"";position:absolute;left:0;right:0;bottom:-8px;height:2px;background:var(--wood)}

/* hero */
.hero{left:0;top:102px;width:1200px;height:397px;background:linear-gradient(90deg,#f4f5f6 0%,#dfe2e5 45%,#c3c8ce 100%)}
.hero-pet{left:46px;top:0;width:402px;height:397px;background:radial-gradient(ellipse at 50% 45%,#f7f4f0 0%,#e9e3dc 55%,rgba(220,222,225,0) 80%)}
.hero-ring{left:722px;top:62px;width:220px;height:220px;border-radius:50%;background:rgba(255,255,255,.28)}
.hero-title{left:571px;top:128px;font-family:"Questrial",sans-serif;font-weight:400;font-size:41px;line-height:50px;color:#2e2e2e;letter-spacing:.5px;white-space:nowrap}
.hero-dots{left:573px;top:245px;display:flex;gap:6px}
.hero-dots span{width:10px;height:10px;border-radius:50%;background:var(--white)}
.hero-dots span.on{background:var(--wood)}

/* intro */
.intro{left:150px;top:515px;width:900px;text-align:center;font-weight:700;font-size:19px;line-height:29px;color:var(--navy)}

/* tiles */
.tile{width:307px;height:210px;overflow:hidden}
.tile-photo{width:100%;height:100%}
.tile-label{position:absolute;left:0;bottom:0;width:100%;height:28px;background:var(--wood);color:var(--white);font-weight:700;font-size:13px;letter-spacing:.8px;text-transform:uppercase;text-align:center;line-height:28px;white-space:nowrap}
.tile-label.navy{background:var(--navy)}

/* news */
.section-title{font-family:"Questrial",sans-serif;font-weight:400;font-size:28px;color:var(--ink)}
.section-title em{font-style:normal;color:var(--navy)}
.news-title{left:94px;top:1358px}
.news-rule{left:94px;top:1406px;width:1012px;height:1px;background:var(--line)}
.news-rule-accent{left:94px;top:1405px;width:90px;height:3px;background:var(--navy)}
.news-arrows{left:1066px;top:1365px}
.news-item{width:494px}
.date-box{position:absolute;left:0;top:0;width:60px;height:80px;background:var(--wood);color:var(--white);text-align:center;border-radius:2px}
.date-day{font-weight:700;font-size:25px;line-height:30px;padding-top:6px}
.date-rest{font-weight:700;font-size:12px;line-height:15px}
.news-body{position:absolute;left:79px;top:0;width:415px}
.news-body h3{font-weight:700;font-size:15px;color:var(--ink);margin-bottom:9px}
.news-body p{font-size:12.5px;line-height:19px;color:#555}
.btn-outline{display:inline-block;border:1px solid var(--wood);color:var(--wood);font-size:12px;padding:2px 10px;text-decoration:none;background:var(--white)}
.news-body .btn-outline{margin-top:8px}
.news-divider{height:1px;background:#e6e6e6}

/* about */
.about{left:0;top:1732px;width:1200px;height:270px;background:var(--grey-band)}
.about-title{left:0;top:1764px;width:1200px;text-align:center}
.about-rule{left:94px;top:1812px;width:1012px;height:1px;background:var(--line)}
.about-rule-accent{left:575px;top:1810px;width:50px;height:3px;background:var(--navy)}
.about-text{left:94px;top:1836px;width:1012px;text-align:center;font-size:17.5px;line-height:28.5px;color:var(--grey-text)}
.about-btn{left:558px;top:1948px}
.about-btn .btn-outline{font-size:12px;padding:2px 9px}

/* footer */
.site-footer{left:0;top:2002px;width:1200px;height:271px;background:var(--footer)}
.foot-head{font-family:"Questrial",sans-serif;font-size:17px;color:var(--white);text-transform:uppercase;letter-spacing:.5px;padding-bottom:9px;border-bottom:1px solid #555}
.quick-links{left:94px;top:2034px;width:205px}
.quick-links ul{list-style:none;display:grid;grid-template-columns:112px 75px;column-gap:0;margin-top:6px}
.quick-links li{font-size:14px;color:#e8e8e8;padding:7px 0 8px;border-bottom:1px solid #2e2e2e}
.inquiry{left:398px;top:2034px;width:208px}
.field{border:1px solid #ddd;height:31px;margin-top:10px;font-style:italic;font-size:13px;color:#e0e0e0;padding:6px 4px}
.field.tall{height:58px}
.field:first-of-type{margin-top:12px}
.submit{margin-top:11px;margin-left:123px;width:85px;height:26px;background:var(--navy);color:var(--white);font-weight:700;font-size:13px;line-height:26px;text-align:center;border:1px solid #aab}
.follow{left:709px;top:2034px;width:152px}
.social{list-style:none;margin-top:8px}
.social li{display:flex;align-items:center;gap:9px;height:39.5px;font-weight:700;font-size:12px;color:var(--white);text-transform:uppercase;letter-spacing:.4px}
.social .dot{width:26px;height:26px;border-radius:50%}
.foot-divider{top:2026px;width:1px;height:220px;background:#2a2a2a}
.foot-circle{left:958px;top:2011px;width:146px;height:146px;border-radius:50%;background:#3a3a3a}
.copyright{left:0;top:2273px;width:1200px;height:44px;background:var(--footer-bottom);border-top:1px solid #2a2a2a;text-align:center;color:var(--white);font-weight:700;font-size:11.5px;line-height:44px}
</style>
</head>
<body>
<div class="page">

  <header class="site-header abs">
    <nav class="main-nav abs">
      <a class="active" href="#" style="left:432px">Home</a>
      <a href="#" style="left:508px">Events</a>
      <a href="#" style="left:587px">Blog</a>
      <a href="#" style="left:654px">Dog Wash</a>
      <a href="#" style="left:760px">Products</a>
      <a href="#" style="left:861px">Resources</a>
      <a href="#" style="left:969px">Links</a>
      <a href="#" style="left:1038px">Contact</a>
    </nav>
    <div class="brand abs"><span class="brand-dot"></span><span class="brand-name">Larkfield Critter Depot</span></div>
  </header>

  <section class="hero abs">
    <div class="hero-pet abs" role="img" aria-label="Smiling white and brown dog raising a paw"></div>
    <div class="hero-ring abs"></div>
    <h1 class="hero-title abs">Dedicated To A Better Diet<br>For A Healthier Pet</h1>
    <div class="hero-dots abs"><span class="on"></span><span></span><span></span><span></span></div>
  </section>

  <p class="intro abs">Lorem ipsum dolor sit amet, consectetur adipiscing elit mauris at porta libero, vitae commodo dui vestibulum sed eros eget magna aliquet iaculis in vitae lorem</p>

  <div class="tile abs" style="left:94px;top:604px"><div class="tile-photo" role="img" aria-label="Pink plush dog toy" style="background:linear-gradient(135deg,#f1ecea,#d94a9c 55%,#e9e4e2)"></div><div class="tile-label navy">Vast Selection of Toys</div></div>
  <div class="tile abs" style="left:446px;top:604px"><div class="tile-photo" role="img" aria-label="Leashes, collars and training gear" style="background:linear-gradient(135deg,#4a5a7e,#6c7c8c 50%,#c0643a)"></div><div class="tile-label">Training Tools</div></div>
  <div class="tile abs" style="left:798px;top:604px"><div class="tile-photo" role="img" aria-label="Bone shaped dog biscuits" style="background:linear-gradient(135deg,#e2c39a,#c99a66 60%,#edd6b6)"></div><div class="tile-label">Treats</div></div>

  <div class="tile abs" style="left:94px;top:838px"><div class="tile-photo" role="img" aria-label="Colourful pet bowls and ball toys" style="background:linear-gradient(135deg,#f3eee6,#3aa0d8 50%,#e56b3a)"></div><div class="tile-label">Other Supplies</div></div>
  <div class="tile abs" style="left:446px;top:838px"><div class="tile-photo" role="img" aria-label="Golden retriever being washed" style="background:linear-gradient(135deg,#dfe6ea,#b98a55 55%,#eef1f2)"></div><div class="tile-label">Dog Washing</div></div>
  <div class="tile abs" style="left:798px;top:838px"><div class="tile-photo" role="img" aria-label="Cat relaxing in a white towel at a spa" style="background:linear-gradient(135deg,#f4f4f2,#e6e3de 60%,#d99a5a)"></div><div class="tile-label">Spa for Pets</div></div>

  <div class="tile abs" style="left:94px;top:1075px"><div class="tile-photo" role="img" aria-label="Grey dog drinking from a bowl on grass" style="background:linear-gradient(135deg,#2f3b55,#7a8088 50%,#5b9a3a)"></div><div class="tile-label">Pup Brew</div></div>
  <div class="tile abs" style="left:446px;top:1075px"><div class="tile-photo" role="img" aria-label="Pet food bag beside scales of justice" style="background:linear-gradient(135deg,#0e2340,#1d4a78 55%,#a57a32)"></div><div class="tile-label">Kibblecrest Lawsuit</div></div>
  <div class="tile abs" style="left:798px;top:1075px"><div class="tile-photo" role="img" aria-label="Community pet food bank emblem" style="background:linear-gradient(135deg,#f0f0ef,#e8e8e6)"></div><div class="tile-label">Harbor Community Food Bank</div></div>

  <h2 class="section-title news-title abs">Recent <em>News &amp; Events</em></h2>
  <svg class="news-arrows abs" width="42" height="26" viewBox="0 0 42 26" aria-hidden="true"><path d="M14 3 L4 13 L14 23" fill="none" stroke="#555" stroke-width="2"/><path d="M28 3 L38 13 L28 23" fill="none" stroke="#555" stroke-width="2"/></svg>
  <div class="news-rule abs"></div>
  <div class="news-rule-accent abs"></div>

  <article class="news-item abs" style="left:94px;top:1430px">
    <div class="date-box"><div class="date-day">01</div><div class="date-rest">Jan<br>2016</div></div>
    <div class="news-body"><h3>Lorem Ipsum Dolor&nbsp; Consecte</h3><p>Sed ut perspiciatis unde omnis iste natus error sit voluptatem accusantium doloremque laudantium, totam rem aperiam, eaque ipsa quae ab illo inventore veritatis et quasi architecto beatae</p><a class="btn-outline" href="#">read more</a></div>
  </article>
  <article class="news-item abs" style="left:612px;top:1430px">
    <div class="date-box"><div class="date-day">01</div><div class="date-rest">Jan<br>2016</div></div>
    <div class="news-body"><h3>Lorem Ipsum Dolor&nbsp; Consecte</h3><p>Sed ut perspiciatis unde omnis iste natus error sit voluptatem accusantium doloremque laudantium, totam rem aperiam, eaque ipsa quae ab illo inventore veritatis et quasi architecto beatae</p><a class="btn-outline" href="#">read more</a></div>
  </article>
  <div class="news-divider abs" style="left:173px;top:1569px;width:415px"></div>
  <div class="news-divider abs" style="left:691px;top:1569px;width:415px"></div>
  <article class="news-item abs" style="left:94px;top:1592px">
    <div class="date-box"><div class="date-day">30</div><div class="date-rest">Dec<br>2015</div></div>
    <div class="news-body"><h3>Lorem Ipsum Dolor&nbsp; Consecte</h3><p>Duis autem vel eum iriure dolor in hendrerit inmo vulputate velit esse molestie consequatn vel illum dolore eu feugiat nulla facilisis...</p><a class="btn-outline" href="#">read more</a></div>
  </article>
  <article class="news-item abs" style="left:612px;top:1592px">
    <div class="date-box"><div class="date-day">30</div><div class="date-rest">Dec<br>2015</div></div>
    <div class="news-body"><h3>Lorem Ipsum Dolor&nbsp; Consecte</h3><p>Duis autem vel eum iriure dolor in hendrerit inmo vulputate velit esse molestie consequatn vel illum dolore eu feugiat nulla facilisis...</p><a class="btn-outline" href="#">read more</a></div>
  </article>

  <section class="about abs"></section>
  <h2 class="section-title about-title abs">About <em>Us</em></h2>
  <div class="about-rule abs"></div>
  <div class="about-rule-accent abs"></div>
  <p class="about-text abs">Lorem ipsum dolor sit amet, consectetur adipiscing elit. Mauris at porta libero, vitae commodo dui. Vestibulum sed eros<br>eget magna aliquet iaculis in vitae lorem. Nunc sed eros quis lacus pharetra consequat non in erat.<br>Curabitur semper nisi dolor, at cursus sapien rutrum et</p>
  <div class="about-btn abs"><a class="btn-outline" href="#">Read More</a></div>

  <footer class="site-footer abs"></footer>
  <div class="foot-divider abs" style="left:350px"></div>
  <div class="foot-divider abs" style="left:660px"></div>
  <div class="foot-divider abs" style="left:910px"></div>

  <div class="quick-links abs">
    <div class="foot-head">Quick Links</div>
    <ul>
      <li>Home</li><li>Products</li>
      <li>Events</li><li>Resources</li>
      <li>Blog</li><li>Links</li>
      <li>About</li><li>Contact</li>
      <li style="border-bottom:none">Dog Wash</li>
    </ul>
  </div>

  <div class="inquiry abs">
    <div class="foot-head">Quick Inquiry</div>
    <div class="field">Full Name</div>
    <div class="field">Email</div>
    <div class="field tall">Message</div>
    <div class="submit">SUBMIT &rsaquo;</div>
  </div>

  <div class="follow abs">
    <div class="foot-head">Follow Us On</div>
    <ul class="social">
      <li><span class="dot" style="background:#3b5a96"></span>Chatterleaf</li>
      <li><span class="dot" style="background:#2a9fd6"></span>Peepline</li>
      <li><span class="dot" style="background:#a0765a"></span>Snapgrove</li>
      <li><span class="dot" style="background:#d8402e"></span>Searchwell</li>
    </ul>
  </div>

  <div class="foot-circle abs"></div>

  <div class="copyright abs">Copyright &copy; 2016 Larkfield Critter Depot . All Rights Reserved.</div>
</div>
</body>
</html>
```